KAZ Freightworks #ALLKAZ Business Cards & Letterhead

I am looking to business cards designed for our organization. We are currently undergoing a small re-branding that is taking place. Our organization is called KAZ Freightworks and we are headquartered in Phoenix, AZ. We primarily provide transportation and logistics services to the Meridel Parcel Bureau who is our largest customer. I would like to see a design that incorporates name, title, contact info, website, and address (this will be different depending on the employee). I would also like to see some color on the business card using our logo colors or a variation. I would like our logo on the back of the business card with the website displayed. The final design should communicate that we are a next generation transportation operate that focuses on being driver-first, customer-centric, innovative, and sustainable.We would also like our #ALLKAZ catch phrase incorporated as well.
Updates

Decision maker traveling outside of the country until Monday, November 25th.

Target Market(s)

Transportation & Logistics

Industry/Entity Type

Trucking Company

Contact Information for Business Card

-First and Last Name
-Position Title
-Contact Phone
-Contact Email
-Physical Address

Font styles to use
Serif

Colors

Designer to choose colors to be used in the design.

Requirements
Must have
• -KAZ logo prominently displayed
• -#ALLKAZ catch phrase used
• -Some amount of color, design gradient, etc.
• -Logo on the back with website listed (https://www.kazfreightco.example)

```html
<!DOCTYPE html>
<html lang="en">
<head>
<meta charset="utf-8">
<title>KAZ Freightworks Business Card</title>
<link rel="stylesheet" href="https://fonts.googleapis.com/css2?family=Questrial&family=Open+Sans:wght@400;600&display=swap">
<style>
  :root {
    --teal: #013b47;
    --green: #79c143;
    --paper: #f7f7f7;
    --ink: #0f3d44;
    --backdrop: #e6e4e0;
  }
  * { box-sizing: border-box; margin: 0; padding: 0; }
  html, body { width: 1200px; height: 900px; overflow: hidden; }
  body {
    background: var(--backdrop);
    display: flex;
    flex-direction: column;
    align-items: center;
    justify-content: center;
    gap: 44px;
    font-family: "Questrial", sans-serif;
  }
  .card {
    width: 630px;
    height: 360px;
    position: relative;
    overflow: hidden;
    box-shadow: 0 6px 18px rgba(0,0,0,.18);
  }
  /* Front */
  .card-front { background: var(--paper); }
  .brand-mark {
    position: absolute; left: 34px; top: 74px;
    display: flex; align-items: center; gap: 10px;
    color: var(--ink); font-size: 40px; letter-spacing: 1px;
  }
  .brand-ring { width: 30px; height: 30px; border: 4px solid var(--green); border-radius: 50%; }
  .person { position: absolute; left: 34px; top: 150px; color: var(--ink); }
  .person-name { font-size: 46px; letter-spacing: 2px; line-height: 1; }
  .person-title { font-size: 22px; letter-spacing: 1.5px; margin: 8px 0 0 60px; }
  .contact {
    position: absolute; left: 330px; top: 110px;
    border-left: 2px solid var(--ink);
    padding: 6px 0 6px 14px;
    list-style: none;
    font-family: "Open Sans", sans-serif; font-size: 11.5px; color: var(--ink);
  }
  .contact li { display: flex; align-items: center; gap: 10px; height: 30px; }
  .contact svg { width: 16px; height: 16px; fill: var(--ink); flex: none; }
  .tag-band {
    position: absolute; right: 0; top: 0; bottom: 0; width: 104px;
    background: var(--teal);
    display: flex; align-items: center; justify-content: center;
  }
  .tag-band span {
    writing-mode: vertical-rl; transform: rotate(180deg);
    color: var(--green); font-size: 46px; letter-spacing: 3px;
  }
  /* Back */
  .card-back {
    background: var(--teal);
    display: flex; flex-direction: column; align-items: center; justify-content: center;
    color: #fff;
  }
  .back-mark { display: flex; align-items: center; gap: 20px; font-size: 96px; letter-spacing: 4px; line-height: 1; }
  .back-mark .brand-ring { width: 60px; height: 60px; border: 7px solid #fff; }
  .back-url { margin-top: 54px; font-family: "Open Sans", sans-serif; font-size: 24px; letter-spacing: 1px; }
</style>
</head>
<body>
  <section class="card card-front">
    <div class="brand-mark"><span class="brand-ring"></span><span>KAZ</span></div>
    <div class="person">
      <p class="person-name">Rowan Teller</p>
      <p class="person-title">CEO Representative</p>
    </div>
    <ul class="contact">
      <li><svg viewBox="0 0 24 24"><path d="M6.6 10.8a15 15 0 0 0 6.6 6.6l2.2-2.2a1 1 0 0 1 1-.25 11.4 11.4 0 0 0 3.6.57 1 1 0 0 1 1 1V20a1 1 0 0 1-1 1A17 17 0 0 1 3 4a1 1 0 0 1 1-1h3.5a1 1 0 0 1 1 1c0 1.25.2 2.45.57 3.57a1 1 0 0 1-.25 1z"/></svg>+1 555 014 2270</li>
      <li><svg viewBox="0 0 24 24"><path d="M12 2a7 7 0 0 0-7 7c0 5.2 7 13 7 13s7-7.8 7-13a7 7 0 0 0-7-7zm0 9.5A2.5 2.5 0 1 1 12 6.5a2.5 2.5 0 0 1 0 5z"/></svg>Street Name, City, Country</li>
      <li><svg viewBox="0 0 24 24"><path d="M2 5h20v14H2z M2 5l10 8 10-8" fill="var(--ink)"/><path d="M3 6l9 7 9-7" fill="none" stroke="#f7f7f7" stroke-width="1.5"/></svg>info@kazfreightco.example</li>
      <li><svg viewBox="0 0 24 24"><path d="M5 3l14 7-6 2 4 7-3 2-4-7-5 4z"/></svg>www.kazfreightco.example</li>
    </ul>
    <div class="tag-band"><span>#ALLKAZ</span></div>
  </section>

  <section class="card card-back">
    <div class="back-mark"><span class="brand-ring"></span><span>KAZ</span></div>
    <p class="back-url">www.kazfreightco.example</p>
  </section>
</body>
</html>
```